STEM business card project for a STEM teacher

I need a business card that is colourful, alive and different to describe my enthusiasm and passion for STEM (Science, Technology, Engineering and Mathematics) teaching
I would like to use specific graphics on the rear of the card. An example of the is can be seen here

https://www.pixorvane.com.au/find?q=stem+logo&img=1#ref=QWTa771mK2

https://www.pixorvane.com.au/find?q=stem+logo&img=1#ref=ZBn40dVcE8

https://www.pixorvane.com.au/find?q=stem+logo&img=1#ref=YpRt93uJx5

Neil Dorrance
STEM Teacher
Marbleford School
0415 738 204

• Something that reflects the exciting and changing nature of STEM education
• Eduction is about enabling students to see what they can do and to let them achieve their full potential
• I m absolutely passionate about letting kids enjoy themselves and see how they can use STEM to positively change their world

```html
<!DOCTYPE html>
<html lang="en">
<head>
<meta charset="utf-8">
<title>Kestrel STEM Lab – Business Card</title>
<link rel="stylesheet" href="https://fonts.googleapis.com/css2?family=Saira+Semi+Expanded:wght@500;600;800&family=Saira+Expanded:wght@400&display=swap">
<style>
  :root {
    --backdrop: #262626;
    --card-white: #ffffff;
    --card-black: #121212;
    --ink-light: #f2f2f2;
    --accent-red: #e5202e;
    --brand-blue: #2b3594;
    --divider: #d9d9d9;
    --shadow: rgba(0,0,0,.55);
  }
  * { box-sizing: border-box; margin: 0; padding: 0; }
  html, body {
    width: 1200px; height: 1200px; overflow: hidden;
    background: var(--backdrop);
  }
  .canvas {
    width: 1200px; height: 1200px;
    display: flex; flex-direction: column;
    align-items: center; justify-content: center; gap: 56px;
  }
  .card {
    width: 840px; height: 480px;
    box-shadow: 0 18px 40px var(--shadow);
  }

  /* Front: brand name in place of the client mark */
  .card-front {
    background: var(--card-white);
    display: flex; align-items: center; justify-content: center; gap: 36px;
    padding: 0 60px;
  }
  .brand-square {
    width: 150px; height: 150px; flex: none;
    background: var(--brand-blue);
  }
  .brand-name {
    font-family: "Saira Semi Expanded", sans-serif;
    font-weight: 800; font-size: 84px; line-height: 0.98;
    color: var(--brand-blue);
    text-transform: uppercase; letter-spacing: 1px;
  }

  /* Back: identity and contact details */
  .card-back {
    background: var(--card-black);
    display: flex; align-items: center; justify-content: center;
    padding-right: 40px;
  }
  .identity {
    text-align: right; padding-right: 32px; margin-top: -110px;
  }
  .person-name {
    font-family: "Saira Semi Expanded", sans-serif;
    font-weight: 600; font-size: 38px; color: var(--ink-light); line-height: 1.05;
  }
  .person-role {
    font-family: "Saira Semi Expanded", sans-serif;
    font-weight: 500; font-size: 24px; color: var(--accent-red);
  }
  .divider {
    width: 2px; height: 210px; background: var(--divider);
  }
  .contact {
    padding-left: 28px; color: var(--ink-light);
    font-family: "Saira Expanded", sans-serif;
    font-size: 21px; letter-spacing: 1.5px; line-height: 1.35;
  }
  .address { margin-bottom: 14px; }
  .contact-line { display: flex; align-items: center; gap: 14px; }
  .contact-line svg { width: 24px; height: 22px; fill: var(--accent-red); flex: none; }
</style>
</head>
<body>
<main class="canvas">
  <section class="card card-front">
    <div class="brand-square"></div>
    <div class="brand-name">Kestrel<br>STEM Lab</div>
  </section>

  <section class="card card-back">
    <div class="identity">
      <div class="person-name">Martin Ashcombe</div>
      <div class="person-role">Managing Director</div>
    </div>
    <div class="divider"></div>
    <div class="contact">
      <div class="address">48 Fernhill Road<br>Glenmoor Heights 3187</div>
      <div class="contact-line">
        <svg viewBox="0 0 24 22" aria-hidden="true"><path d="M2 7c0-3 5-5 10-5s10 2 10 5v2h-5V7H7v2H2z"/><path d="M5 11h14l2 9H3z"/></svg>
        <span>03.5521.6408</span>
      </div>
      <div class="contact-line">
        <svg viewBox="0 0 24 22" aria-hidden="true"><rect x="6" y="1" width="12" height="6"/><rect x="1" y="8" width="22" height="9" rx="2"/><rect x="6" y="14" width="12" height="7"/></svg>
        <span>03.5521.6419</span>
      </div>
      <div class="contact-line">
        <svg viewBox="0 0 24 22" aria-hidden="true"><path d="M1 3h22v16H1z M3 5l9 7 9-7" fill="none" stroke="#e5202e" stroke-width="2"/></svg>
        <span>hello@kestrelstem.net</span>
      </div>
      <div class="contact-line">
        <svg viewBox="0 0 24 22" aria-hidden="true"><circle cx="12" cy="11" r="10"/><path d="M2 11h20M12 1c-4 4-4 16 0 20M12 1c4 4 4 16 0 20" fill="none" stroke="#121212" stroke-width="1.5"/></svg>
        <span>www.kestrelstem.net</span>
      </div>
    </div>
  </section>
</main>
</body>
</html>
```